KDTA Lantern Theatre "The Harvest"

I want to create a postcard to be used in marketing for our theatre season.

I will upload some images on Power Point that are to be suggestions for the art work.

I will also include a Word document that has the pertinent information to be included.

```html
<!DOCTYPE html>
<html lang="en">
<head>
<meta charset="utf-8">
<title>KDTA Lantern Theatre – The Harvest Postcard</title>
<link rel="stylesheet" href="https://fonts.googleapis.com/css2?family=Cinzel:wght@400;600&family=Fira+Sans+Extra+Condensed:ital,wght@0,600;1,400&display=swap">
<style>
  :root {
    --paper: #ffffff;
    --edge: #1a1a1a;
    --stage-deep: #3a0d0d;
    --stage-mid: #8c1a1a;
    --stage-glow: #c8201f;
    --curtain-light: #e8201c;
    --curtain-dark: #a30d0d;
    --mask-gold: #d4b240;
    --mask-shade: #a8842a;
    --gold-text: #f7d400;
    --rule: #1a1a1a;
  }
  * { margin: 0; padding: 0; box-sizing: border-box; }
  html, body {
    width: 1200px;
    height: 930px;
    overflow: hidden;
    background: var(--paper);
  }
  .postcard {
    position: relative;
    width: 1200px;
    height: 930px;
    background: var(--paper);
    border: 1px solid var(--edge);
  }
  .promo-panel {
    position: absolute;
    left: 0;
    top: 0;
    width: 580px;
    height: 766px;
    background: radial-gradient(ellipse 62% 60% at 50% 58%, var(--stage-glow) 0%, var(--stage-mid) 55%, var(--stage-deep) 100%);
    overflow: hidden;
  }
  .curtain-valance {
    position: absolute;
    left: 0;
    top: 0;
    width: 580px;
    height: 132px;
    background: linear-gradient(180deg, var(--curtain-light) 0%, var(--curtain-dark) 100%);
    border-radius: 0 0 50% 50% / 0 0 28% 28%;
  }
  .theatre-masks {
    position: absolute;
    left: 208px;
    top: 122px;
    width: 178px;
    height: 116px;
    background: linear-gradient(135deg, var(--mask-gold) 0%, var(--mask-shade) 100%);
    border-radius: 40% 40% 48% 48%;
  }
  .promo-text {
    position: absolute;
    left: 0;
    width: 580px;
    text-align: center;
    color: var(--gold-text);
    text-shadow: 2px 3px 4px rgba(40, 0, 0, 0.75);
  }
  .presenter {
    top: 284px;
    font-family: "Cinzel", serif;
    font-weight: 600;
    font-size: 37px;
    letter-spacing: 1px;
    line-height: 1;
  }
  .presents {
    top: 325px;
    font-family: "Cinzel", serif;
    font-weight: 600;
    font-size: 22px;
    line-height: 1;
  }
  .season-title {
    top: 358px;
    font-family: "Cinzel", serif;
    font-weight: 600;
    font-size: 54px;
    line-height: 1;
  }
  .season-years {
    top: 421px;
    font-family: "Cinzel", serif;
    font-weight: 600;
    font-size: 34px;
    line-height: 1;
  }
  .info-lead {
    top: 522px;
    font-family: "Fira Sans Extra Condensed", sans-serif;
    font-style: italic;
    font-weight: 400;
    font-size: 27px;
    line-height: 1;
  }
  .contact-name,
  .contact-email {
    font-family: "Fira Sans Extra Condensed", sans-serif;
    font-weight: 600;
    font-size: 29px;
    line-height: 1;
  }
  .contact-name { top: 565px; }
  .contact-email { top: 607px; }
  .stamp-box {
    position: absolute;
    left: 1033px;
    top: 29px;
    width: 138px;
    height: 185px;
    border: 1px solid var(--rule);
  }
  .address-lines {
    position: absolute;
    left: 0;
    top: 0;
  }
</style>
</head>
<body>
  <main class="postcard">
    <section class="promo-panel">
      <div class="curtain-valance" role="img" aria-label="Draped red stage curtain valance"></div>
      <div class="theatre-masks" role="img" aria-label="Gold comedy and tragedy theatre masks"></div>
      <h1 class="promo-text presenter">KDTA Lantern Theatre</h1>
      <p class="promo-text presents">Presents</p>
      <h2 class="promo-text season-title">“The Harvest”</h2>
      <p class="promo-text season-years">2014-2015</p>
      <p class="promo-text info-lead">For more information on any performance,&nbsp; contact</p>
      <p class="promo-text contact-name">Dana Whitlow</p>
      <p class="promo-text contact-email">dwhitlow@lanternarts.example.org</p>
    </section>

    <div class="stamp-box"></div>

    <svg class="address-lines" width="1200" height="930" viewBox="0 0 1200 930" aria-hidden="true">
      <g stroke="var(--rule)" stroke-width="1.2">
        <line x1="666" y1="376.5" x2="1170" y2="376.5"/>
        <line x1="666" y1="470.5" x2="1170" y2="470.5"/>
        <line x1="666" y1="565.5" x2="1170" y2="565.5"/>
        <line x1="900" y1="659.5" x2="1170" y2="659.5"/>
      </g>
    </svg>
  </main>
</body>
</html>
```